Nexolite Pane VDI Brochure Design for IT Company

We are looking for an 4 page A4 brochure (A3 size folded in half).

We are an IT company based in Adelaide Australia and are promoting Nexolite Virtual Desktop Environments to medical practices (small, medium and large). As doctors and practice managers do not like to receive cold sales calls or emails - we would like to design up a 'high quality' brochure that will grab their attention!

The brochure will be mailed out and directed to practice managers - so the front page need to be captivating.

I will upload some text that we have come up with - this may not be the final wording, but will get the ball rolling. The 'amount' of text / dot points will be similar.

We would like to include quite a few pictures, because no one wants to read though a pile of text all piled together.

The text needs to be separated into "easy-to-read" sections throughout the brochure, highlighting on important aspects. For example the customer testimonials, The 'Happy' section, 'from ANY computer or device ANYTIME' etc.

Our traditional colour scheme can be found on our website at www.trellowbyte.com.au, however we are not too fussed for this project - as long as our logos are prominent throughout the design.

I have included several 'sample' images - basically just ones that were found on Plimbo images + a few we took ourselves. Feel free to find and/or use your alternate images.

We definitely need to use pictures that feature doctor(s) using an Tabrix - this should maybe be the focus on the front cover. We would also like a close-up picture of an Tabrix inside with the medical software superimposed onto the screen (we have taken our own photo - but it's not great, and also uploaded a screen-shot of the medical software to superimpose on a higher quality Tabrix photo stock).

A couple of the pictures we would like to be prominent are the qTorn client (or more so the size of it - the picture with the client in someone’s hand. And the Tabrix picture(s) - doctors will like the ability to work from an Tabrix for anywhere.

Included are a selection of our company logos - these can be modified to suit whatever colour scheme you design.

Thanks in advance - Mark.

Target Market(s)

Doctors and Practice Managers of Medical and Health Centres

Industry/Entity Type

Computer

Requirements
Must have
• Pictures of doctors using Tabrixes
Pictures of the QTORN client with the hand under it (to show the size)
Separated text blocks/sections for readability

```html
<!DOCTYPE html>
<html lang="en">
<head>
<meta charset="utf-8">
<title>Nexolite Pane brochure spread</title>
<link href="https://fonts.googleapis.com/css2?family=Open+Sans:wght@400;600;700&family=Roboto+Condensed:wght@400;700&display=swap" rel="stylesheet">
<style>
:root{
  --orange:#f26a1b;
  --blue:#1f5fae;
  --ink:#3b3b3b;
  --page-grey:#ededed;
  --band-grey:#d6d6d6;
  --column-grey:#e4e4e4;
  --white:#ffffff;
}
*{box-sizing:border-box;margin:0;padding:0}
html,body{width:1200px;height:875px;overflow:hidden;background:var(--white)}
body{font-family:"Open Sans",Arial,sans-serif;color:var(--ink)}
.spread{position:absolute;left:40px;top:28px;width:1120px;height:820px;display:flex}
.page{position:relative;width:560px;height:820px;overflow:hidden}
.page-left{background:var(--page-grey)}
.page-left .top-band{position:absolute;left:0;top:0;width:100%;height:110px;background:linear-gradient(var(--band-grey),var(--page-grey))}
.page-right{background:var(--white)}
.headline{position:absolute;left:48px;top:138px;width:240px;font-family:"Roboto Condensed",Arial,sans-serif;font-weight:400;font-size:25px;line-height:1.05;color:var(--orange)}
.section-title{font-family:"Roboto Condensed",Arial,sans-serif;font-size:25px;line-height:1.05;color:var(--orange);font-weight:400;margin-bottom:10px}
.column{position:absolute;font-size:8px;line-height:1.36}
.column p{margin-bottom:7px}
.column .lead{color:var(--orange);font-weight:600}
.column .question{color:var(--blue);font-weight:700}
.column-one{left:48px;top:200px;width:240px}
.column-two{left:306px;top:138px;width:230px}
.product-photo{position:absolute;left:306px;top:548px;width:230px;height:195px;background:radial-gradient(ellipse at 50% 55%,#fafafa 0%,#dcdcdc 55%,#c9b8a8 100%)}
.brand-row{position:absolute;left:48px;bottom:34px;display:flex;align-items:center;gap:18px;font-weight:700;font-size:18px;color:#58595b}
.brand-row .mark{width:22px;height:22px;background:var(--orange)}
.brand-row .divider{width:1px;height:26px;background:#9a9a9a}
.photo-column{position:absolute;left:24px;top:0;width:190px;height:820px}
.photo{position:absolute;left:0;width:190px;box-shadow:0 2px 6px rgba(0,0,0,.25)}
.photo-doctors{top:22px;height:300px;background:linear-gradient(160deg,#e9eef3,#b9c6d3 60%,#8b9aa7)}
.photo-tablet{top:340px;height:220px;background:linear-gradient(150deg,#cfcfcf,#8d8d8d 55%,#5d6a73)}
.photo-xray{top:578px;height:225px;background:linear-gradient(170deg,#eef2f4,#bfd0d8 55%,#7e8d97)}
.accent{position:absolute;left:214px;width:8px;background:var(--orange)}
.info-column{position:absolute;left:232px;top:0;width:328px;height:820px;background:var(--column-grey)}
.happy-title{position:absolute;left:18px;width:170px;height:30px;background:var(--orange);color:var(--white);font-family:"Roboto Condensed",Arial,sans-serif;font-weight:700;font-size:16px;line-height:30px;padding-left:10px}
.happy-list{position:absolute;left:22px;width:285px;list-style:none;font-size:9.2px;line-height:1.45}
.happy-list li{padding-left:8px;position:relative}
.happy-list li::before{content:"•";position:absolute;left:0}
</style>
</head>
<body>
<div class="spread">
  <section class="page page-left">
    <div class="top-band"></div>
    <h1 class="headline">Is your IT infrastructure still in the 1990’s?</h1>
    <div class="column column-one">
      <p class="lead">If you’re using standard desktops or Terminal Services to access your Medical applications, then it’s a good chance that Trellowbyte can help. Moving to a Virtual Desktop Infrastructure will reduce your costs, increase your productivity and make all of your staff happy!</p>
      <p class="lead">Lower overheads, less downtime, access anywhere, print anywhere, always up-to-date – these are just a few of the features a Nexolite solution by Trellowbyte Consulting can offer your practice.</p>
      <p class="question">Sick of after-hours updates?</p>
      <p class="question">Sick of annoying pop-ups telling you Flarex Flash, Flarex Reader, Jolt, Mirosa Paneos, MedChart updates are waiting to be updated?</p>
      <p class="question">Sick of having different versions of Mirosa Office and other applications on different computers?</p>
      <p class="question">Sick of not being able to install a printer to the building?</p>
      <p class="question">Sick of server downtime causing productivity losses?</p>
      <p class="lead">Wanting to be able to instantly access your desktop from any computer or device anytime.</p>
      <p>With a VDI solution from Trellowbyte Consulting your doctors, nurses, admin and management staff can swap rooms with in your establishment and access their exact desktop. Securely log in from your home PC or Orchard laptop or desktop and still access your usual desktop. Print documents, letters and scripts from home or any printer anywhere – no setup necessary – they just work! Access your usual desktop from your Tabrix, Droidex or Paneos tablet – giving you the ability to consult anywhere!</p>
    </div>
    <div class="column column-two">
      <h2 class="section-title">How does it work?</h2>
      <p>Traditionally most medical practices run a client/server or a peer to peer network. This infrastructure is now quickly becoming antiquated in favour of newer virtualised solutions. Nexolite Pane is software that allows you to move your desktop operating systems and applications to your server or datacentre, consolidating your IT environment.</p>
      <p>With your desktops now hosted on your server/s, you can access them anywhere on multiple devices. Desktop clients can be replaced as they reach their end of life with Zero Clients.</p>
      <p>Zero clients are very small and inexpensive devices used for accessing your desktop. They have no moving parts and the speed at which they run is controlled by your server equipment. Therefore they basically never have to be upgraded or replaced once deployed. As it’s even hard to store data on their individual workstations this opens up an opportunity for data loss and/or medico legal issues when disposing of equipment. As Nexolite Pane stores ALL data on the server/s this eliminates this threat.</p>
      <p>We configure Nexolite Pane in a ‘linked clone’ configuration. This allows us to only have to install applications once. All of the users’ desktops are ‘linked’ to this clone. This provides a much similar management solution and drastically cuts down on labour costs involved in installation, updating and maintaining a number of individual desktops. A linked-clone environment will also provide end users with a consistent experience across multiple desktops and devices.</p>
    </div>
    <div class="product-photo" role="img" aria-label="Photo of a small qTorn zero client box resting in an open hand to show its size"></div>
    <div class="brand-row">
      <span class="mark"></span><span>Trellowbyte</span>
      <span class="divider"></span>
      <span>Nexolite</span>
    </div>
  </section>

  <section class="page page-right">
    <div class="photo-column">
      <div class="photo photo-doctors" role="img" aria-label="Photo of a group of smiling doctors in white coats"></div>
      <div class="photo photo-tablet" role="img" aria-label="Photo of a hand holding a Tabrix tablet showing medical software"></div>
      <div class="photo photo-xray" role="img" aria-label="Photo of a doctor reviewing an x-ray image"></div>
    </div>
    <div class="accent" style="top:60px;height:90px"></div>
    <div class="accent" style="top:400px;height:70px"></div>
    <div class="accent" style="top:640px;height:80px"></div>

    <div class="info-column">
      <div class="happy-title" style="top:92px">Doctors Happy:</div>
      <ul class="happy-list" style="top:135px">
        <li>All Medical and Electronic Reference Material</li>
        <li>Always up to date</li>
        <li>No wait time to access their software (from home, work or mobile devices)</li>
        <li>Printing available from any offsite PC</li>
        <li>Access to their desktop from any device anytime</li>
        <li>All workstations operate exactly the same performance</li>
        <li>All workstations have all of the practices third-party applications installed and configured</li>
      </ul>
      <div class="happy-title" style="top:400px">Admin Staff Happy:</div>
      <ul class="happy-list" style="top:443px">
        <li>Easily swap doctors to different locations with no fuss</li>
        <li>No helping doctors with printer issues in different locations</li>
        <li>Can concentrate on helping patients and not on IT issues</li>
      </ul>
      <div class="happy-title" style="top:562px">Management Happy:</div>
      <ul class="happy-list" style="top:605px">
        <li>Lower overheads</li>
        <li>Easier to budget (Zero Clients at $399.00 Each)</li>
        <li>Less downtime for server maintenance</li>
        <li>All Data resides on the server/s / datacentre with allows ALL data to be backed-up (including end-user virtual desktops)</li>
        <li>Power consumption up to 80% less with Zero clients</li>
      </ul>
    </div>
  </section>
</div>
</body>
</html>
```